Ridgeline Talent Associates Business Card Design

We need a business card design for our new company - Ridgeline Talent Associates. RLTA is a recruitment firm that focuses on recruiting engineers and geologist for mid-size oil and gas companies. We would like our logo on the business card, which is attached, and we would like the color scheme on business cards to coordinate with our logo.

Industry/Entity Type

Oil And Gas

Contact Information for Business Card

Dana Whitlow, Founder and Managing Partner, dmw@ridgelinetalentco.org, 888.507.3942 (work), 5730915.0600 (cell), 573.642.1907 (fax), www.ridgelinetalentco.org

```html
<!DOCTYPE html>
<html lang="en">
<head>
<meta charset="utf-8">
<title>Ridgeline Talent Associates – Business Card</title>
<link rel="stylesheet" href="https://fonts.googleapis.com/css2?family=Open+Sans:wght@400;600;700&display=swap">
<style>
  :root {
    --page-bg: #e9eaee;
    --card-white: #ffffff;
    --navy: #1c3a78;
    --navy-deep: #1a2d5e;
    --navy-light: #24498e;
    --strip-dark: #2a2b30;
    --text-white: #ffffff;
    --faint-mark: #e6e7ee;
    --shadow: rgba(40, 45, 60, 0.12);
  }
  * { box-sizing: border-box; margin: 0; padding: 0; }
  html, body { width: 1200px; height: 600px; overflow: hidden; }
  body {
    background: var(--page-bg);
    font-family: "Open Sans", Arial, sans-serif;
    position: relative;
  }
  .card {
    position: absolute;
    top: 152px;
    width: 467px;
    height: 278px;
    border-radius: 16px;
    overflow: hidden;
    background: var(--card-white);
    box-shadow: 0 6px 18px var(--shadow);
  }
  .card--front { left: 93px; }
  .card--back { left: 638px; }

  /* Front */
  .card--front .brand {
    position: absolute;
    left: 0; right: 0; top: 118px;
    display: flex; align-items: center; justify-content: center; gap: 10px;
  }
  .brand-dot {
    width: 18px; height: 18px; border-radius: 50%;
    background: var(--navy);
  }
  .brand-name {
    color: var(--navy);
    font-weight: 600;
    font-size: 21px;
    letter-spacing: 0.2px;
    white-space: nowrap;
  }

  /* Back */
  .back-top {
    position: absolute; left: 0; top: 0; width: 100%; height: 140px;
    background: var(--card-white);
  }
  .back-top .brand {
    position: absolute; left: 18px; top: 78px;
    display: flex; align-items: center; gap: 8px;
  }
  .back-top .brand-dot { width: 14px; height: 14px; }
  .back-top .brand-name { font-size: 15.5px; }
  .faint-mark {
    position: absolute; right: 20px; top: -10px;
    width: 170px; height: 170px; border-radius: 50%;
    background: var(--faint-mark);
  }
  .divider-strip {
    position: absolute; left: 0; top: 140px; width: 100%; height: 6px;
    background: var(--strip-dark);
  }
  .contact-panel {
    position: absolute; left: 0; top: 146px; width: 100%; height: 132px;
    background: linear-gradient(180deg, var(--navy-light) 0%, var(--navy) 45%, var(--navy-deep) 100%);
    color: var(--text-white);
  }
  .panel-notch {
    position: absolute; left: 48px; top: 146px;
    width: 0; height: 0;
    border-left: 9px solid transparent;
    border-right: 9px solid transparent;
    border-top: 11px solid var(--strip-dark);
  }
  .person {
    position: absolute; left: 18px; top: 16px;
  }
  .person-name { font-size: 15.5px; font-weight: 600; line-height: 20px; }
  .person-title { font-size: 11.5px; line-height: 16px; }
  .contact-list {
    position: absolute; left: 268px; top: 16px;
    list-style: none; font-size: 11px; line-height: 18px;
  }
  .contact-list b { font-weight: 700; }
  .contact-list .gap { margin-top: 3px; }
  .contact-list .web { margin-top: 9px; font-weight: 700; }
</style>
</head>
<body>
  <section class="card card--front" aria-label="Card front">
    <div class="brand">
      <span class="brand-dot"></span>
      <span class="brand-name">Ridgeline Talent Associates</span>
    </div>
  </section>

  <section class="card card--back" aria-label="Card back">
    <div class="back-top">
      <div class="faint-mark" role="img" aria-label="Faint brand decoration"></div>
      <div class="brand">
        <span class="brand-dot"></span>
        <span class="brand-name">Ridgeline Talent Associates</span>
      </div>
    </div>
    <div class="divider-strip"></div>
    <div class="contact-panel">
      <div class="person">
        <p class="person-name">Dana Whitlow</p>
        <p class="person-title">Founder and Managing Partner</p>
      </div>
      <ul class="contact-list">
        <li><b>Office:</b> 888.507.3942</li>
        <li><b>Fax:</b> 573.642.1907</li>
        <li><b>Mobile:</b> 5730915.0600</li>
        <li class="gap"><b>Email:</b> dmw@ridgelinetalentco.org</li>
        <li class="web">www.ridgelinetalentco.org</li>
      </ul>
    </div>
    <div class="panel-notch"></div>
  </section>
</body>
</html>
```